Powerpoint template for basic scientists studying immunology

We are an QVA-funded consortium of basic science researchers at academic centers in Boston, Philadelphia and Oxford, UK. We study why the immune system fails to get rid of Hepatitis C virus, and whether new antiviral treatments that reduce viral load improve immune function. We are looking for a powerpoint template that we can use as a "brand" for our research consortium. It would feature a logo (file attached) and should represent the fonts/colors contained in the logo. We we would present at meetings and to program officers at the QVA, but, if we ever get around to it, would also be on a website.

The scientific description is as follows:
Hepatitis C virus (HCV) infects 185 million persons worldwide, is the leading indication for liver transplantation and, in the US, has a higher mortaliy rate than HIV. The annual healthcare costs associated with HCV exceed $9 billion, a number expected to increase as the epidemic matures and end stage liver disease peaks over the next decade. By virtue of its remarkable predilection for persistence, HCV is a model chronic viral infection. Mounting evidence supports the idea that HCV, while inducing type I IFN expression, maintains chronicity by virtue of global suppression of host innate and adaptive immunity. The mainstay of treatment for the last two decades, IFN-α-based regimens are ineffective in many patient subgroups and have significant side effects. The recent development of highly effective direct acting antivirals (DAA) against HCV promises to alter the landscape of this devastating infection by offering curative therapy without IFN. However, it remains essential that we understand what type of immunity remains following pharmacological eradication of the virus because: a) many HCV infected subjects remain at risk for re-infection; and b) DAAs are only partially effective in some patient subgroups, particularly those with past treatment with IFN. The imminent availability of IFN-free treatment for HCV offers an unprecedented opportunity to understand broad questions about alterations in immunity in humans with cure of chronic infections. Until now, mechanistic dissection of human immune responses has been challenging due to limited ability to directly perturb the system. The organizing principle of this U19 Program therefore, is to capitalize on the unique opportunity to, for the first time, cure chronic viral infection in humans without immune modulation and interrogate the immunological changes that ensue. Thus, we have formulated the following central hypothesis for this Program: DAA-mediated cure of chronic HCV infection will lead to partial "resetting" of some immune abnormalities, but specific immunological defects will persist in some subjects that prevent development of optimal immunity to HCV. We will test this hypothesis through a set of integrated Projects and Cores.

Target Market(s)

scientists.

Industry/Entity Type

Biotechnology

Font styles to use
Sans Serif

Requirements
Must have
• Very clean, very simple. Mostly whitespace for puting graphs and data on. Colors, fonts should match the logo. Please see ppt example.
Should not have
• too much of the ppt covered with the logo.

```html
<!DOCTYPE html>
<html lang="en">
<head>
<meta charset="utf-8">
<title>BATF binds to target genes</title>
<link href="https://fonts.googleapis.com/css2?family=Arimo:wght@400;700&display=swap" rel="stylesheet">
<style>
  :root {
    --brand-blue: #0b9fd9;
    --brand-green: #6a9f1f;
    --ink: #1a1a1a;
    --nav-grey: #c9ced6;
    --paper: #ffffff;
  }
  html, body {
    margin: 0;
    padding: 0;
    width: 1200px;
    height: 900px;
    overflow: hidden;
    background: var(--paper);
    font-family: "Arimo", Arial, sans-serif;
  }
  .slide {
    position: relative;
    width: 1200px;
    height: 900px;
    background: var(--paper);
  }
  .brand {
    position: absolute;
    left: 22px;
    top: 26px;
    display: flex;
    align-items: center;
    gap: 10px;
  }
  .brand-square {
    width: 22px;
    height: 22px;
    background: var(--brand-green);
  }
  .brand-name {
    font-size: 24px;
    font-weight: 700;
    color: var(--brand-blue);
    letter-spacing: 0.5px;
  }
  .header-rule {
    position: absolute;
    left: 150px;
    top: 67px;
    width: 990px;
    height: 3px;
    background: var(--brand-blue);
  }
  .slide-title {
    position: absolute;
    left: 0;
    top: 222px;
    width: 1190px;
    margin: 0;
    text-align: center;
    font-weight: 400;
    font-size: 43px;
    line-height: 58px;
    color: var(--brand-blue);
  }
  .slide-title .keyword { color: var(--brand-green); }
  .charts {
    position: absolute;
    left: 0;
    top: 0;
    width: 1200px;
    height: 900px;
  }
  .charts text { font-family: "Arimo", Arial, sans-serif; fill: var(--ink); }
  .axis { stroke: var(--ink); stroke-width: 2; fill: none; }
  .series { stroke: var(--ink); stroke-width: 2.4; fill: none; }
  .point { fill: var(--ink); }
  .leader { stroke: var(--ink); stroke-width: 0.8; stroke-dasharray: 2 2; fill: none; }
  .chart-title { font-size: 16px; }
  .tick-label { font-size: 11px; }
  .axis-label { font-size: 14px; }
  .series-label { font-size: 10px; }
  .nav { position: absolute; left: 0; top: 0; width: 1200px; height: 900px; pointer-events: none; }
  .nav-icon { fill: var(--nav-grey); }
</style>
</head>
<body>
<main class="slide">
  <div class="brand">
    <span class="brand-square"></span>
    <span class="brand-name">Corvane</span>
  </div>
  <div class="header-rule"></div>

  <h1 class="slide-title"><span class="keyword">BATF</span> binds to target genes<br>within 24 hours of differentiation</h1>

  <svg class="charts" viewBox="0 0 1024 768" aria-label="ChIP binding of BATF over three days in WT and BATF KO P14 cells">
    <!-- WT chart -->
    <g class="chart chart-wt">
      <text class="chart-title" x="364" y="356" text-anchor="middle">WT P14</text>
      <path class="axis" d="M268 357 V530 H442 M263 357 H268 M263 444 H268 M263 530 H268 M268 530 V535 M326 530 V535 M384 530 V535 M442 530 V535"/>
      <text class="tick-label" x="261" y="361" text-anchor="end">0.2</text>
      <text class="tick-label" x="261" y="448" text-anchor="end">0.1</text>
      <text class="tick-label" x="261" y="534" text-anchor="end">0.0</text>
      <text class="tick-label" x="268" y="548" text-anchor="middle">0</text>
      <text class="tick-label" x="326" y="548" text-anchor="middle">1</text>
      <text class="tick-label" x="384" y="548" text-anchor="middle">2</text>
      <text class="tick-label" x="442" y="548" text-anchor="middle">3</text>
      <text class="axis-label" x="370" y="566" text-anchor="middle">Days after Stimulation</text>
      <text class="tick-label" transform="translate(222 444) rotate(-90)" text-anchor="middle">% Input</text>

      <polyline class="series" points="268,521 326,403 384,391 442,420"/>
      <polyline class="series" points="268,521 326,442 384,452 442,431"/>
      <polyline class="series" points="268,526 326,473 384,466 442,496"/>
      <polyline class="series" points="268,527 326,516 384,506 442,519"/>
      <g class="point">
        <circle cx="268" cy="521" r="5"/><circle cx="326" cy="403" r="5"/><circle cx="384" cy="391" r="5"/><circle cx="442" cy="420" r="5"/>
        <circle cx="326" cy="442" r="5"/><circle cx="384" cy="452" r="5"/><circle cx="442" cy="431" r="5"/>
        <circle cx="268" cy="526" r="5"/><circle cx="326" cy="473" r="5"/><circle cx="384" cy="466" r="5"/><circle cx="442" cy="496" r="5"/>
        <circle cx="326" cy="516" r="5"/><circle cx="384" cy="506" r="5"/><circle cx="442" cy="519" r="5"/>
      </g>
      <text class="series-label" x="456" y="424">Bcl2</text>
      <text class="series-label" x="453" y="443">CTLA4</text>
      <text class="series-label" x="453" y="500">IL2Ra</text>
      <text class="series-label" x="453" y="526">IL10</text>
    </g>

    <!-- KO chart -->
    <g class="chart chart-ko">
      <text class="chart-title" x="705" y="356" text-anchor="middle">BATF KO P14</text>
      <path class="axis" d="M598 357 V530 H770 M593 357 H598 M593 444 H598 M593 530 H598 M598 530 V535 M655 530 V535 M712 530 V535 M770 530 V535"/>
      <text class="tick-label" x="591" y="361" text-anchor="end">0.2</text>
      <text class="tick-label" x="591" y="448" text-anchor="end">0.1</text>
      <text class="tick-label" x="591" y="534" text-anchor="end">0.0</text>
      <text class="tick-label" x="598" y="548" text-anchor="middle">0</text>
      <text class="tick-label" x="655" y="548" text-anchor="middle">1</text>
      <text class="tick-label" x="712" y="548" text-anchor="middle">2</text>
      <text class="tick-label" x="770" y="548" text-anchor="middle">3</text>
      <text class="axis-label" x="690" y="570" text-anchor="middle">Days after Stimulation</text>

      <polyline class="series" points="598,507 655,509 712,524 770,525"/>
      <polyline class="series" points="598,512 655,513 712,525 770,526"/>
      <polyline class="series" points="598,518 655,516 712,526 770,527"/>
      <polyline class="series" points="598,519 655,517 712,527 770,528"/>
      <g class="point">
        <circle cx="598" cy="507" r="5"/><circle cx="598" cy="512" r="5"/><circle cx="598" cy="518" r="5"/>
        <circle cx="655" cy="509" r="5"/><circle cx="655" cy="516" r="5"/>
        <circle cx="712" cy="525" r="5"/><circle cx="770" cy="525" r="5"/><circle cx="770" cy="528" r="5"/>
      </g>
      <path class="leader" d="M776 522 L784 494 M776 524 L784 510 M776 526 L784 526 M776 528 L784 542"/>
      <text class="series-label" x="786" y="494">Bcl2</text>
      <text class="series-label" x="786" y="511">CTLA4</text>
      <text class="series-label" x="786" y="528">IL2Ra</text>
      <text class="series-label" x="786" y="549">IL10</text>
    </g>
  </svg>

  <svg class="nav" viewBox="0 0 1024 768" aria-hidden="true">
    <path class="nav-icon" d="M10 746 L16 741 V744 H24 V748 H16 V751 Z"/>
    <path class="nav-icon" d="M46 752 L54 742 L57 745 L49 755 L45 756 Z"/>
    <rect class="nav-icon" x="78" y="742" width="14" height="2"/>
    <rect class="nav-icon" x="78" y="746" width="14" height="2"/>
    <rect class="nav-icon" x="78" y="750" width="14" height="2"/>
    <path class="nav-icon" d="M126 746 L120 741 V744 H112 V748 H120 V751 Z"/>
  </svg>
</main>
</body>
</html>
```